Fashion Company Business Card

Style// Minimalism (Less is more)
Colour// No required colour. If you use a solid colour, vigorous violet is preferred, or any other mix of fashionable patterns. Purple reference to http://cdn.pixelmarten.example.s3.cloudvault.example/blog/Famous-Purple-Logos/11-famous-purple-logos.jpg)
Font// any matching sans serif fonts (logo is helveica neue light)
Contents// as following
- logo
- (website) www.velorbe.example
- (add) 3870 Marsh Ln, Suite 417 Toronto ON M4K 1P8
- (Office phone) +1 416 555 0187
- (email) info@velorbe.example
- (social media logos: Facebook, Instagram, Twitter, Tumblr, Vimeo, Youtube) @Velorbe/@Velorbemedia
- (slogan)│Fashion│Art│Unique
*optional - QR code
- (personal info) For example
Dora Ketts
Founder & Creative Director
c. XXX.XXX.XXXX
Please submit jpg file for selecting, and submit a psd file for editing personal info for different employers after selected. If you need more information, please email doraketts@velorbe.example.

```html
<!DOCTYPE html>
<html lang="en">
<head>
<meta charset="utf-8">
<title>Velorbe – Business Card</title>
<link rel="stylesheet" href="https://fonts.googleapis.com/css2?family=Inter:wght@300;400&display=swap">
<style>
  :root {
    --page-bg: #ecebee;
    --card-white: #ffffff;
    --lilac-soft: #e9e2f1;
    --lilac-mid: #d9cde8;
    --blush: #f1dbe6;
    --ink: #111111;
    --band-grey: #d3d3d3;
    --icon-grey: #b9bbbe;
    --text-grey: #333333;
  }
  * { box-sizing: border-box; margin: 0; padding: 0; }
  html, body {
    width: 1200px; height: 1000px; overflow: hidden;
    background: var(--page-bg);
    font-family: "Inter", "Helvetica Neue", Arial, sans-serif;
    color: var(--ink);
  }
  .canvas { position: relative; width: 1200px; height: 1000px; }
  .card {
    position: absolute; left: 190px; width: 820px; height: 470px;
    background: var(--card-white);
    box-shadow: 0 4px 18px rgba(0,0,0,.12);
    overflow: hidden;
  }
  .card--front { top: 20px; }
  .card--back { top: 510px; }

  .card__pattern {
    position: absolute; inset: 0;
    background:
      linear-gradient(180deg, var(--lilac-mid) 0%, var(--lilac-soft) 14%, rgba(255,255,255,0) 38%),
      linear-gradient(0deg, var(--lilac-mid) 0%, var(--lilac-soft) 16%, rgba(255,255,255,0) 42%),
      radial-gradient(ellipse at 8% 12%, var(--blush) 0%, rgba(255,255,255,0) 28%),
      var(--card-white);
  }

  .wordmark {
    position: absolute; left: 0; right: 0; text-align: center;
    font-weight: 300; letter-spacing: .08em; color: var(--ink);
  }
  .card--front .wordmark { top: 190px; font-size: 72px; }
  .card--back .wordmark { top: 92px; font-size: 50px; }

  .website {
    position: absolute; left: 0; right: 0; top: 154px; text-align: center;
    font-size: 18px; font-weight: 400;
  }
  .slogan-band {
    position: absolute; left: 0; right: 0; top: 184px; height: 46px;
    background: var(--band-grey);
    display: flex; align-items: center; justify-content: center;
    font-size: 28px; font-weight: 300; letter-spacing: .28em;
    color: var(--text-grey);
  }
  .person {
    position: absolute; left: 40px; top: 246px; width: 380px; text-align: center;
  }
  .person__name { font-size: 32px; font-weight: 400; }
  .person__title { font-size: 24px; font-weight: 300; margin-top: 6px; }
  .person__mobile { font-size: 22px; font-weight: 300; margin-top: 4px; }

  .office {
    position: absolute; left: 430px; top: 262px; width: 370px; text-align: center;
    font-size: 18px; font-weight: 300; line-height: 1.4; font-style: normal;
  }
  .office__contact { margin-top: 14px; }
  .office__dot {
    display: inline-block; width: 8px; height: 8px; border-radius: 50%;
    background: var(--ink); margin: 0 6px; vertical-align: middle;
  }

  .social { position: absolute; left: 0; right: 0; top: 388px; text-align: center; }
  .social__icons { display: flex; justify-content: center; gap: 6px; }
  .social__icon { width: 32px; height: 32px; background: var(--icon-grey); }
  .social__handles {
    margin-top: 6px; font-size: 12px; font-weight: 400;
    display: flex; justify-content: center; gap: 28px;
  }
</style>
</head>
<body>
<main class="canvas">

  <section class="card card--front" aria-label="Card front">
    <div class="card__pattern" role="img" aria-label="Soft lilac faceted geometric background pattern with pink brush accents"></div>
    <h1 class="wordmark">VELORBE</h1>
  </section>

  <section class="card card--back" aria-label="Card back">
    <div class="card__pattern" role="img" aria-label="Soft lilac faceted geometric background pattern with pink brush accents"></div>
    <p class="wordmark">VELORBE</p>
    <p class="website">www.velorbe.example</p>
    <div class="slogan-band">STYLE | FORM | VISION</div>

    <div class="person">
      <p class="person__name">Dora Ketts</p>
      <p class="person__title">Founder &amp; Creative Director</p>
      <p class="person__mobile">c. XXX.XXX.XXXX</p>
    </div>

    <address class="office">
      <p>3870 Marsh Ln, Suite 417</p>
      <p>Toronto ON M4K 1P8</p>
      <p class="office__contact">+1 416 555 0187<span class="office__dot"></span>info@velorbe.example</p>
    </address>

    <div class="social">
      <div class="social__icons" aria-label="Social media channels">
        <span class="social__icon"></span>
        <span class="social__icon"></span>
        <span class="social__icon"></span>
        <span class="social__icon"></span>
        <span class="social__icon"></span>
        <span class="social__icon"></span>
      </div>
      <p class="social__handles"><span>@Velorbe</span><span>@Velorbemedia</span></p>
    </div>
  </section>

</main>
</body>
</html>
```